Puravel Cat Litter Logo/Package Concept

We need a logo and packaging design concept for a new brand of paper cat littler.

The product is a paper cat litter that utilises special technology to offer superior Odour and moisture absorption - making it more pleasant for customers to clean and have in their home.

It is also Biodegradable and made from Recycled Material so it is friendly to the environment and customers can feel good that they are making an ethical, responsible choice for their cat's litter.

The litter granules are also particularly appealing to cats.

Target Market(s)

Females 25-45 years, cat owners

Industry/Entity Type

Pet Care

Colors
fbed22
9bcb3b
00a990
0492cd
266eb0
6a439a

Requirements
Must have
• - A concept for the Puravel logo
• - Product title in a large, prominent spot on the front "Paper"
• - Feel; clean, fresh, crisp, simple, inviting, anti-bacterial, sparkling, bright,
• - A close-up picture of the actual litter granules
• - A caricature of a cat OR a photo of a real cat.
• - image imposed on a 3D bag, example supplied. Can use alternative image if preferred.
Nice to have
• The ability for the design to be adapted to expand into crystal/clay littler once we introduce more products into the range.
Should not have
• anything to do with dogs
• feel to natural, holistic, earthy or dull.

```html
<!DOCTYPE html>
<html lang="en">
<head>
<meta charset="utf-8">
<title>Puravel Paper Cat Litter – Pack Front</title>
<link rel="stylesheet" href="https://fonts.googleapis.com/css2?family=Londrina+Solid:wght@400;900&family=Roboto+Slab:wght@700;800&family=Nunito:wght@800;900&display=swap">
<style>
  :root {
    --teal: #1fa596;
    --teal-deep: #16897d;
    --yellow: #fbd823;
    --orange: #f26a1b;
    --white: #ffffff;
    --granule-light: #d9d2c2;
    --granule-dark: #8f887a;
  }
  * { box-sizing: border-box; margin: 0; padding: 0; }
  html, body { width: 876px; height: 1200px; overflow: hidden; }
  body { background: var(--teal); }
  .pack {
    position: relative;
    width: 876px;
    height: 1200px;
    background: var(--teal);
    overflow: hidden;
    font-family: "Nunito", sans-serif;
  }
  .brand {
    position: absolute;
    top: 96px; left: 0; width: 100%;
    text-align: center;
    font-family: "Londrina Solid", sans-serif;
    font-weight: 900;
    font-size: 92px;
    letter-spacing: 2px;
    color: var(--yellow);
    line-height: 1;
  }
  .title-band {
    position: absolute;
    left: 158px; top: 244px;
    width: 546px; height: 112px;
    background: var(--orange);
    transform: rotate(-1.5deg);
  }
  .title {
    position: absolute;
    top: 224px; left: 0; width: 100%;
    text-align: center;
    font-family: "Londrina Solid", sans-serif;
    font-weight: 900;
    font-size: 188px;
    line-height: 1;
    letter-spacing: 4px;
    color: var(--white);
  }
  .subtitle {
    position: absolute;
    top: 430px; left: 0; width: 100%;
    text-align: center;
    font-family: "Londrina Solid", sans-serif;
    font-weight: 400;
    font-size: 104px;
    line-height: 1;
    letter-spacing: 2px;
    color: var(--white);
  }
  .granules {
    position: absolute;
    left: 225px; top: 558px;
    width: 428px; height: 428px;
    border-radius: 50%;
    border: 6px solid var(--yellow);
    background: radial-gradient(circle at 45% 40%, var(--granule-light), #bfb7a6 60%, var(--granule-dark));
  }
  .badge-icon {
    position: absolute;
    border-radius: 50%;
    border: 4px solid var(--yellow);
    background: var(--teal);
  }
  .badge-icon svg { width: 100%; height: 100%; display: block; }
  .badge-icon--eco { left: 75px; top: 885px; width: 152px; height: 152px; }
  .badge-icon--odour { left: 530px; top: 855px; width: 136px; height: 136px; }
  .pointer { position: absolute; left: 240px; top: 920px; width: 130px; height: 160px; }
  .eco-label {
    position: absolute;
    left: 30px; top: 1030px;
    width: 258px; height: 98px;
    background: var(--white);
    border-radius: 26px;
    text-align: center;
    font-family: "Roboto Slab", serif;
    font-weight: 800;
    color: var(--teal-deep);
    padding-top: 10px;
    line-height: 1.15;
  }
  .eco-label__lead { display: block; font-size: 25px; }
  .eco-label__rest { display: block; font-size: 18px; font-weight: 700; }
  .tech-note {
    position: absolute;
    right: 70px; top: 895px;
    text-align: right;
    font-family: "Roboto Slab", serif;
    font-weight: 700;
    font-size: 22px;
    line-height: 1.1;
    color: var(--white);
  }
  .benefit {
    position: absolute;
    left: 572px; width: 238px;
  }
  .benefit--odour {
    top: 968px; height: 76px;
    background: var(--yellow);
    color: var(--white);
    font-size: 50px; font-weight: 900;
    line-height: 76px;
    padding-left: 14px;
  }
  .benefit--moisture {
    top: 1044px; height: 90px;
    background: var(--white);
    color: var(--teal-deep);
    display: flex; align-items: center;
    padding-left: 12px;
  }
  .benefit__plus { font-size: 52px; font-weight: 900; margin-right: 10px; line-height: 1; }
  .benefit__text { font-size: 27px; font-weight: 800; line-height: 1.05; }
</style>
</head>
<body>
  <main class="pack">
    <div class="brand">PURAVEL</div>

    <div class="title-band" role="img" aria-label="Orange brush stroke behind the product title"></div>
    <h1 class="title">PAPER</h1>
    <h2 class="subtitle">CAT LITTLER</h2>

    <div class="granules" role="img" aria-label="Close-up photo of paper litter granules"></div>

    <div class="badge-icon badge-icon--eco">
      <svg viewBox="0 0 100 100" fill="none" stroke="#fff" stroke-width="3" stroke-linecap="round" stroke-linejoin="round">
        <path d="M42 28 L50 16 L58 28"/>
        <path d="M62 34 L72 52"/>
        <path d="M70 62 L56 76 L70 76"/>
        <path d="M44 76 L28 76 L36 62"/>
        <path d="M30 54 L40 36"/>
        <path d="M42 58 C42 46 54 42 62 40 C60 50 56 60 44 60 Z"/>
        <path d="M44 60 L54 48"/>
      </svg>
    </div>

    <svg class="pointer" viewBox="0 0 130 160" fill="none" stroke="#fbd823" stroke-width="5" stroke-linecap="round" stroke-linejoin="round">
      <path d="M10 150 C60 140 100 100 102 30"/>
      <path d="M88 44 L102 26 L114 46"/>
    </svg>

    <p class="eco-label">
      <span class="eco-label__lead">Biodegradable</span>
      <span class="eco-label__rest">and made from<br>Recycled Material</span>
    </p>

    <div class="badge-icon badge-icon--odour">
      <svg viewBox="0 0 100 100" fill="none" stroke="#fff" stroke-width="4" stroke-linecap="round">
        <path d="M34 30 C26 38 42 46 34 54 C26 62 42 70 34 74"/>
        <path d="M50 26 C42 34 58 42 50 50 C42 58 58 66 50 70"/>
        <path d="M66 30 C58 38 74 46 66 54 C58 62 74 70 66 74"/>
      </svg>
    </div>

    <p class="tech-note">Special<br>technology</p>

    <div class="benefit benefit--odour">+Odour</div>
    <div class="benefit benefit--moisture">
      <span class="benefit__plus">+</span>
      <span class="benefit__text">moisture<br>absorption</span>
    </div>
  </main>
</body>
</html>
```